Brightmoor Co Trade Show Flyer

We need a brochure design (8.5 x 11) Info in the design (refer to rough draft I drew on Paper): "#1 selling tool to aquire new franchisees has been video testimonials" - Martin L. Greaves, C.E.O Kolva Smoothie Franchise Testimonials - Let your franchisees do the selling for you. Franchisee testimonial: $10,000 / per Franchisee Includes: • 2 minute Video • 1 minute add for your franchise's location • Concept creation • Communication with franchisee • Travel to their location • All rental equipment • 1 round of corrections • Animated logo • Licensed music ******* For 25% Discount section (next to middle box), please put the "Venture Fairground Logo" Great to use on all your social media (USE logos and icons) • Website • Clipcast • Proflow • Friendlo • Snapgrid • Chirper • Phone calls • Emails • In person meetings Some of our clients: (use the logos I uploaded - in round boxes as in draft) LOGO (Brightmoor Franchise Testimonial) www.brightmoorstories.example (866) 555-0187

Target Market(s)

Franchise owners

Colors

Designer to choose colors to be used in the design.

Requirements

```html
<!DOCTYPE html>
<html lang="en">
<head>
<meta charset="utf-8">
<title>Brightmoor Co – Franchise Testimonials Flyer</title>
<link href="https://fonts.googleapis.com/css2?family=Bebas+Neue&family=Montserrat:wght@500;600;700;800&family=Zilla+Slab:wght@700&display=swap" rel="stylesheet">
<style>
  :root{
    --bg:#eceae6;
    --blue:#0a7fc0;
    --navy:#0d3a52;
    --navy-deep:#0a2a3c;
    --yellow:#eed900;
    --gold-top:#ffe600;
    --gold-bottom:#ffa800;
    --teal:#00ab91;
    --teal-text:#00a08a;
    --ink-blue:#0d5aa0;
    --white:#ffffff;
  }
  *{box-sizing:border-box;margin:0;padding:0}
  html,body{width:1200px;height:2504px;overflow:hidden;background:var(--bg)}
  .flyer{
    position:absolute;left:50px;top:541px;width:1100px;height:1422px;
    background:var(--white);box-shadow:0 8px 24px rgba(0,0,0,.18);overflow:hidden;
    font-family:"Montserrat",sans-serif;
  }
  .quote-band{
    position:absolute;left:0;top:0;width:100%;height:159px;background:var(--blue);
    display:flex;align-items:center;justify-content:center;text-align:center;
    font-family:"Zilla Slab",serif;font-weight:700;color:var(--white);
    font-size:39px;line-height:46px;letter-spacing:.3px;
  }
  .hero{
    position:absolute;left:0;top:169px;width:100%;height:424px;
    background:linear-gradient(135deg,#0f4a66 0%,#0b3650 45%,#123f52 70%,#0a2d40 100%);
  }
  .hero-title{position:absolute;left:0;top:0;width:100%;text-align:center;font-family:"Bebas Neue",sans-serif}
  .hero-title .line-1{display:block;color:var(--white);font-size:166px;line-height:1;margin-top:42px;letter-spacing:1px}
  .hero-title .line-2{
    display:block;font-size:212px;line-height:1;margin-top:-18px;
    background:linear-gradient(180deg,var(--gold-top) 20%,var(--gold-bottom) 95%);
    -webkit-background-clip:text;background-clip:text;color:transparent;
  }
  .package{
    position:absolute;left:0;top:631px;width:689px;height:522px;background:var(--yellow);
    border-radius:0 44px 44px 0;padding:28px 0 0 50px;color:var(--ink-blue);
  }
  .package h2{font-size:27px;font-weight:700;margin-bottom:22px}
  .package ul{list-style:none}
  .package li{
    display:flex;align-items:flex-start;gap:14px;font-size:25px;font-weight:500;
    line-height:31px;margin-bottom:13px;text-transform:uppercase;
  }
  .package li svg{flex:none;width:30px;height:30px;margin-top:2px}
  .discount{
    position:absolute;left:712px;top:628px;width:362px;height:155px;background:var(--blue);
    border-radius:44px 44px 0 0;color:var(--white);text-align:center;
    font-size:44px;font-weight:700;line-height:52px;padding-top:26px;
  }
  .expo{
    position:absolute;left:712px;top:797px;width:362px;height:347px;background:var(--teal);
    border-radius:0 0 44px 44px;color:var(--white);text-align:center;
  }
  .expo-name{font-family:"Montserrat",sans-serif;font-weight:800;font-size:40px;line-height:40px;text-align:left;padding:26px 0 0 64px}
  .expo-tag{margin:14px auto 0;width:265px;background:rgba(255,255,255,.85);color:var(--teal);font-size:13px;font-weight:800;letter-spacing:1px;line-height:16px}
  .brand{margin-top:26px;display:flex;flex-direction:column;align-items:center}
  .brand-dot{width:52px;height:52px;border-radius:50%;background:var(--white);margin-bottom:12px}
  .brand-name{font-weight:800;font-size:40px;line-height:42px}
  .brand-sub{font-weight:700;font-size:11px;letter-spacing:.5px;margin-top:2px}
  .contact{position:absolute;left:46px;top:1176px;color:var(--teal-text);font-weight:700;font-size:28px}
  .contact p{display:flex;align-items:center;gap:14px;height:48px}
  .contact svg{width:32px;height:32px;flex:none}
  .social{position:absolute;left:585px;top:1182px;width:470px}
  .social h3{color:var(--teal-text);font-size:31px;font-weight:700;margin-bottom:14px;letter-spacing:.3px}
  .social ul{list-style:none;display:flex;justify-content:space-between}
  .social li{display:flex;flex-direction:column;align-items:center;gap:6px;font-size:15px;font-weight:700;color:var(--teal-text)}
  .social li span.dot{width:54px;height:54px;border-radius:50%}
  .dot-a{background:#e02a2a}.dot-b{background:#0d5aa0}.dot-c{background:#2b4f9a}.dot-d{background:#c0367e}.dot-e{background:#35a9e8}
  .trusted{
    position:absolute;left:0;top:1336px;width:100%;height:86px;background:var(--navy-deep);
    display:flex;align-items:center;padding:0 46px;color:var(--white);
  }
  .trusted h4{font-size:29px;font-weight:700;margin-right:auto}
  .trusted ul{list-style:none;display:flex;gap:30px}
  .trusted li{font-size:16px;font-weight:700;color:var(--white)}
</style>
</head>
<body>
<main class="flyer">
  <header class="quote-band">#1 SELLING TOOL TO AQUIRE NEW FRANCHISEES<br>HAS BEEN VIDEO TESTIMONIALS"</header>

  <section class="hero" role="img" aria-label="Dark blue toned photo of city towers and banknotes behind the title">
    <h1 class="hero-title"><span class="line-1">FRANCHISE</span><span class="line-2">TESTIMONIALS</span></h1>
  </section>

  <section class="package">
    <h2>$10,000 / PER FRANCHISEE INCLUDES:</h2>
    <ul>
      <li><svg viewBox="0 0 30 30"><path d="M25 9A12 12 0 1 0 27 15" fill="none" stroke="currentColor" stroke-width="2.6" stroke-linecap="round"/><path d="M9 15l5 5 13-14" fill="none" stroke="currentColor" stroke-width="2.6" stroke-linecap="round" stroke-linejoin="round"/></svg>2 minute video</li>
      <li><svg viewBox="0 0 30 30"><path d="M25 9A12 12 0 1 0 27 15" fill="none" stroke="currentColor" stroke-width="2.6" stroke-linecap="round"/><path d="M9 15l5 5 13-14" fill="none" stroke="currentColor" stroke-width="2.6" stroke-linecap="round" stroke-linejoin="round"/></svg>1 minute add for your franchise's location</li>
      <li><svg viewBox="0 0 30 30"><path d="M25 9A12 12 0 1 0 27 15" fill="none" stroke="currentColor" stroke-width="2.6" stroke-linecap="round"/><path d="M9 15l5 5 13-14" fill="none" stroke="currentColor" stroke-width="2.6" stroke-linecap="round" stroke-linejoin="round"/></svg>Concept creation</li>
      <li><svg viewBox="0 0 30 30"><path d="M25 9A12 12 0 1 0 27 15" fill="none" stroke="currentColor" stroke-width="2.6" stroke-linecap="round"/><path d="M9 15l5 5 13-14" fill="none" stroke="currentColor" stroke-width="2.6" stroke-linecap="round" stroke-linejoin="round"/></svg>Communication with franchisee</li>
      <li><svg viewBox="0 0 30 30"><path d="M25 9A12 12 0 1 0 27 15" fill="none" stroke="currentColor" stroke-width="2.6" stroke-linecap="round"/><path d="M9 15l5 5 13-14" fill="none" stroke="currentColor" stroke-width="2.6" stroke-linecap="round" stroke-linejoin="round"/></svg>Travel to their location</li>
      <li><svg viewBox="0 0 30 30"><path d="M25 9A12 12 0 1 0 27 15" fill="none" stroke="currentColor" stroke-width="2.6" stroke-linecap="round"/><path d="M9 15l5 5 13-14" fill="none" stroke="currentColor" stroke-width="2.6" stroke-linecap="round" stroke-linejoin="round"/></svg>All rental equipment</li>
      <li><svg viewBox="0 0 30 30"><path d="M25 9A12 12 0 1 0 27 15" fill="none" stroke="currentColor" stroke-width="2.6" stroke-linecap="round"/><path d="M9 15l5 5 13-14" fill="none" stroke="currentColor" stroke-width="2.6" stroke-linecap="round" stroke-linejoin="round"/></svg>1 round of corrections</li>
      <li><svg viewBox="0 0 30 30"><path d="M25 9A12 12 0 1 0 27 15" fill="none" stroke="currentColor" stroke-width="2.6" stroke-linecap="round"/><path d="M9 15l5 5 13-14" fill="none" stroke="currentColor" stroke-width="2.6" stroke-linecap="round" stroke-linejoin="round"/></svg>Animated logo</li>
      <li><svg viewBox="0 0 30 30"><path d="M25 9A12 12 0 1 0 27 15" fill="none" stroke="currentColor" stroke-width="2.6" stroke-linecap="round"/><path d="M9 15l5 5 13-14" fill="none" stroke="currentColor" stroke-width="2.6" stroke-linecap="round" stroke-linejoin="round"/></svg>Licensed music</li>
    </ul>
  </section>

  <div class="discount">FOR 25%<br>DISCOUNT</div>

  <section class="expo">
    <p class="expo-name">The Venture<br>Fairground</p>
    <p class="expo-tag">OWN YOUR OWN BUSINESS!</p>
    <div class="brand">
      <span class="brand-dot"></span>
      <span class="brand-name">BRIGHTMOOR</span>
      <span class="brand-sub">FRANCHISE TESTIMONIALS</span>
    </div>
  </section>

  <address class="contact" style="font-style:normal">
    <p><svg viewBox="0 0 32 32" fill="none" stroke="#0d5aa0" stroke-width="2"><circle cx="16" cy="16" r="13"/><ellipse cx="16" cy="16" rx="6" ry="13"/><path d="M3 16h26M5 9h22M5 23h22"/></svg>brightmoorstories.example</p>
    <p><svg viewBox="0 0 32 32" fill="none" stroke="#0d5aa0" stroke-width="2.2"><rect x="3" y="8" width="26" height="17"/><path d="M3 8l13 10 13-10"/></svg>info@brightmoorstories.example</p>
    <p><svg viewBox="0 0 32 32" fill="none" stroke="#0d5aa0" stroke-width="2.2"><circle cx="16" cy="16" r="13"/><path d="M11 9c-2 2-1 6 3 10s8 5 10 3l-3-3-2 1c-2-1-4-3-5-5l1-2z" stroke-linejoin="round"/></svg>(866) 555-0187</p>
  </address>

  <section class="social">
    <h3>ALL YOUR SOCIAL MEDIA</h3>
    <ul>
      <li><span class="dot dot-a"></span>Clipcast</li>
      <li><span class="dot dot-b"></span>Proflow</li>
      <li><span class="dot dot-c"></span>Friendlo</li>
      <li><span class="dot dot-d"></span>Snapgrid</li>
      <li><span class="dot dot-e"></span>Chirper</li>
    </ul>
  </section>

  <footer class="trusted">
    <h4>TRUSTED BY:</h4>
    <ul>
      <li>Dunmore Scoops</li>
      <li>Corner Nine</li>
      <li>Kolva Smoothie</li>
      <li>Tidewell Pro</li>
      <li>Axelton Auto</li>
    </ul>
  </footer>
</main>
</body>
</html>
```